Vex

I have the logo for the back already. Need the front to match.
Need a VEX logo which I can provide or you can download one - VEX Realty in canada... Back of the card will be my logo and name. Front will have the info...
I would like a black background. Match colors on front to the back..
Details on Card

Target Market(s)

Realestate clients.. Keep it classy like the logo

Contact Information for Business Card

Moren Tadwick office - 5817730264 cell - 5819063147 email - Moren@MorenTadwick.Com. website - MorenTadwick.Com Facebook - MTadwRealty Instagram - Moren_Qpl_Realtor Address - 418 - 23 St NE | K5P2M8

Colors
3176b5
33a6d7
85cae6

Requirements
Must have
• same color scheme as the logo
logo will be on the back
Black Background
Horizontal card
The one side of the card should be clean. like I stated, just my logo " Moren Tadwick " and nothing else

```html
<!DOCTYPE html>
<html lang="en">
<head>
<meta charset="utf-8">
<title>Moren Tadwick – Business Card</title>
<link rel="stylesheet" href="https://fonts.googleapis.com/css2?family=Montserrat:wght@400;500&display=swap">
<style>
  :root {
    --page: #1f2124;
    --card: #000000;
    --edge: #3176b5;
    --band: #3176b5;
    --accent: #33a6d7;
    --info-text: #d9d9d9;
    --name-text: #ffffff;
  }
  * { box-sizing: border-box; margin: 0; padding: 0; }
  html, body { width: 1200px; height: 900px; overflow: hidden; }
  body {
    background: var(--page);
    font-family: "Montserrat", Arial, sans-serif;
    display: flex;
    flex-direction: column;
    align-items: center;
    justify-content: center;
    gap: 56px;
  }
  .card {
    position: relative;
    width: 600px;
    height: 343px;
    background: var(--card);
    border: 3px solid var(--edge);
    border-radius: 3px;
  }

  /* Front: contact side */
  .contact-band {
    position: absolute;
    left: 18px;
    top: 0;
    width: 46px;
    height: 290px;
    background: var(--band);
    border-radius: 0 0 23px 23px;
  }
  .contact-list {
    position: absolute;
    left: 18px;
    top: 20px;
    list-style: none;
  }
  .contact-item {
    display: flex;
    align-items: center;
    height: 36px;
  }
  .contact-icon {
    width: 46px;
    display: flex;
    justify-content: center;
  }
  .contact-icon svg { width: 24px; height: 24px; }
  .contact-text {
    margin-left: 22px;
    font-size: 15px;
    font-weight: 400;
    color: var(--info-text);
    letter-spacing: 0.2px;
  }
  .front-brand {
    position: absolute;
    right: 40px;
    bottom: 104px;
    font-size: 18px;
    font-weight: 500;
    color: var(--edge);
    letter-spacing: 2px;
  }
  .front-name {
    position: absolute;
    right: 60px;
    bottom: 48px;
    padding-left: 14px;
    border-left: 2px solid var(--edge);
    font-size: 26px;
    font-weight: 500;
    color: var(--name-text);
    line-height: 1.2;
  }

  /* Back: logo side */
  .back {
    display: flex;
    align-items: center;
    justify-content: center;
  }
  .back-brand {
    font-size: 34px;
    font-weight: 500;
    color: var(--edge);
    letter-spacing: 4px;
  }
</style>
</head>
<body>

<section class="card front" aria-label="Contact side">
  <div class="contact-band"></div>
  <ul class="contact-list">
    <li class="contact-item">
      <span class="contact-icon">
        <svg viewBox="0 0 24 24" fill="none" stroke="#fff" stroke-width="1.4"><circle cx="12" cy="12" r="10.5"/><rect x="7.5" y="8" width="9" height="8" rx="1"/><path d="M9.5 8v-1.5h5V8"/></svg>
      </span>
      <span class="contact-text">5817730264</span>
    </li>
    <li class="contact-item">
      <span class="contact-icon">
        <svg viewBox="0 0 24 24" fill="none" stroke="#fff" stroke-width="1.4"><circle cx="12" cy="12" r="10.5"/><path d="M8.5 7.5l2 2-1 1.5c.8 1.6 1.9 2.7 3.5 3.5l1.5-1 2 2-1.5 1.5c-3.5-.5-7-4-7.5-7.5z"/></svg>
      </span>
      <span class="contact-text">5819063147</span>
    </li>
    <li class="contact-item">
      <span class="contact-icon">
        <svg viewBox="0 0 24 24" fill="none" stroke="#fff" stroke-width="1.4"><circle cx="12" cy="12" r="10.5"/><rect x="7" y="8.5" width="10" height="7" rx="0.8"/><path d="M7 9l5 3.5L17 9"/></svg>
      </span>
      <span class="contact-text">Moren@MorenTadwick.Com</span>
    </li>
    <li class="contact-item">
      <span class="contact-icon">
        <svg viewBox="0 0 24 24" fill="none" stroke="#fff" stroke-width="1.4"><circle cx="12" cy="12" r="10.5"/><circle cx="12" cy="12" r="5.5"/><path d="M6.5 12h11M12 6.5c-2 2.8-2 8.2 0 11M12 6.5c2 2.8 2 8.2 0 11"/></svg>
      </span>
      <span class="contact-text">www.MorenTadwick.Com</span>
    </li>
    <li class="contact-item">
      <span class="contact-icon">
        <svg viewBox="0 0 24 24" fill="none" stroke="#fff" stroke-width="1.4"><circle cx="12" cy="12" r="10.5"/><circle cx="12" cy="12" r="4.5"/></svg>
      </span>
      <span class="contact-text">MTadwRealty</span>
    </li>
    <li class="contact-item">
      <span class="contact-icon">
        <svg viewBox="0 0 24 24" fill="none" stroke="#fff" stroke-width="1.4"><circle cx="12" cy="12" r="10.5"/><rect x="8" y="8" width="8" height="8"/></svg>
      </span>
      <span class="contact-text">Moren_Qpl_Realtor</span>
    </li>
    <li class="contact-item">
      <span class="contact-icon">
        <svg viewBox="0 0 24 24" fill="none" stroke="#fff" stroke-width="1.4"><circle cx="12" cy="12" r="10.5"/><path d="M12 17.5s-4-4.2-4-7a4 4 0 0 1 8 0c0 2.8-4 7-4 7z"/><circle cx="12" cy="10.5" r="1.4"/></svg>
      </span>
      <span class="contact-text">418 - 23 St NE | K5P2M8</span>
    </li>
  </ul>
  <div class="front-brand">MOREN TADWICK</div>
  <div class="front-name">Moren Tadwick</div>
</section>

<section class="card back" aria-label="Logo side">
  <div class="back-brand">MOREN TADWICK</div>
</section>

</body>
</html>
```